Velmar Industrial Coatings

We are looking to improve our business cards. Our company installs industrial floor and wall coatings in industrial, chemical and food processing plants.
Our coatings which consist of epoxy, urethane, and vinyl esters provide chemical and abrasion resistant surface with non-skid properties that are easy to clean.

Target Market(s)

food manufacturing, chemical plants, breweries and wineries, warehouses, clean room floors.

Industry/Entity Type

Construction

Contact Information for Business Card

improved current logo.

Colors

Designer to choose colors to be used in the design.

Requirements
Must have
• the information from uploaded file
Nice to have
• "We'll be outstanding on your floors."

```html
<!DOCTYPE html>
<html lang="en">
<head>
<meta charset="utf-8">
<title>Velmar Industrial Coatings – Business Cards</title>
<link href="https://fonts.googleapis.com/css2?family=Oswald:wght@300;600&family=Questrial&family=Josefin+Sans:wght@600&display=swap" rel="stylesheet">
<style>
  :root{
    --sheet:#eeeeee;
    --navy:#182b49;
    --teal:#0089a8;
    --teal-deep:#00758f;
    --teal-shade:#007a96;
    --aqua:#1fbcc8;
    --aqua-light:#8ed6f2;
    --sky:#8fd8f7;
    --sky-deep:#6cc9f2;
    --white:#ffffff;
    --ink:#3a3a3a;
    --grid-grey:#cfcfcf;
    --deco-grey:#e3e3e5;
  }
  *{margin:0;padding:0;box-sizing:border-box}
  html,body{width:1200px;height:758px;overflow:hidden;background:var(--sheet)}
  .canvas{position:relative;width:1200px;height:758px;background:var(--sheet);overflow:hidden}
  .card{position:absolute;width:597px;height:358px;overflow:hidden}
  .card--front-teal{left:0;top:0;background:var(--teal)}
  .card--back-navy{left:604px;top:0;width:596px;background:var(--navy)}
  .card--front-white{left:0;top:400px;background:var(--white)}
  .card--back-sky{left:604px;top:400px;width:596px;background:var(--sky)}
  .card svg.art{position:absolute;left:0;top:0;width:100%;height:100%}

  .badge{position:absolute;display:flex;flex-direction:column;align-items:center;justify-content:center;text-align:center;
    font-family:"Questrial",sans-serif;font-size:19px;line-height:1.25;color:var(--aqua)}
  .badge--round{width:174px;height:174px;border-radius:50%;background:var(--navy);border:4px solid var(--aqua)}
  .card--front-teal .badge{left:58px;top:50px}
  .card--back-navy .badge,.card--back-sky .badge{left:211px;top:93px}
  .badge--square{left:78px;top:98px;width:136px;height:112px;background:var(--navy);border:4px solid var(--aqua-light);color:var(--aqua-light);font-size:17px}

  .holder{position:absolute;left:0;width:290px;text-align:center}
  .holder__name{top:240px;font-family:"Josefin Sans",sans-serif;font-size:24px;letter-spacing:.5px}
  .holder__name b{font-weight:600}
  .holder__name span{font-family:"Questrial",sans-serif}
  .holder__phone{top:268px;font-family:"Oswald",sans-serif;font-weight:300;font-size:18px}
  .card--front-teal .holder__name b{color:var(--aqua-light)}
  .card--front-teal .holder__name span,.card--front-teal .holder__phone{color:var(--white)}
  .card--front-white .holder__name b{color:var(--teal-deep)}
  .card--front-white .holder__name span,.card--front-white .holder__phone{color:var(--ink)}

  .company{position:absolute;left:292px;top:36px;font-family:"Oswald",sans-serif;line-height:1}
  .company__lead{font-weight:300;font-size:31px;display:block}
  .company__line{font-weight:600;font-size:31px;display:block;margin-top:4px;letter-spacing:-.3px}
  .card--front-teal .company__lead{color:var(--white)}
  .card--front-teal .company__line{color:var(--aqua-light)}
  .card--front-white .company__lead{color:var(--ink)}
  .card--front-white .company__line{color:var(--teal-deep)}

  .contact{position:absolute;left:386px;font-family:"Questrial",sans-serif;color:var(--white);font-size:17px;line-height:20px;letter-spacing:.4px}
  .contact__office{top:128px}
  .contact__office strong{font-family:"Josefin Sans",sans-serif;font-weight:600;color:var(--aqua-light);display:block}
  .card--front-white .contact__office strong{color:var(--aqua-light)}
  .contact__row{position:absolute;left:386px;font-family:"Questrial",sans-serif;color:var(--white);font-size:17px;letter-spacing:.4px}
</style>
</head>
<body>
<main class="canvas">

  <!-- Front, teal -->
  <section class="card card--front-teal">
    <svg class="art" viewBox="0 0 597 358" aria-hidden="true">
      <g stroke="#007a95" stroke-width="16" fill="none" stroke-linecap="round" stroke-linejoin="round">
        <polyline points="485,-5 548,57 605,2"/>
        <polyline points="-8,245 58,310 10,365"/>
      </g>
      <g stroke="#28c2cf" stroke-width="1.4" fill="none" opacity=".85">
        <line x1="0" y1="60" x2="282" y2="60"/><line x1="0" y1="109" x2="338" y2="109"/>
        <line x1="0" y1="159" x2="338" y2="159"/><line x1="0" y1="208" x2="338" y2="208"/>
        <line x1="28" y1="60" x2="28" y2="208"/><line x1="75" y1="43" x2="75" y2="232"/>
        <line x1="213" y1="43" x2="213" y2="232"/><line x1="282" y1="43" x2="282" y2="232"/>
        <line x1="329" y1="159" x2="329" y2="208"/>
        <line x1="0" y1="313" x2="282" y2="313"/>
        <line x1="27" y1="313" x2="27" y2="358"/><line x1="74" y1="297" x2="74" y2="358"/>
        <line x1="143" y1="297" x2="143" y2="358"/><line x1="212" y1="297" x2="212" y2="358"/>
        <line x1="280" y1="297" x2="280" y2="358"/>
        <line x1="282" y1="108" x2="338" y2="108"/>
      </g>
      <g class="info-panels">
        <rect x="364" y="122" width="233" height="70" fill="var(--navy)"/>
        <rect x="364" y="192" width="233" height="3" fill="var(--aqua)"/>
        <rect x="364" y="196" width="233" height="85" fill="var(--navy)"/>
        <rect x="364" y="281" width="233" height="3" fill="var(--aqua)"/>
        <rect x="364" y="285" width="233" height="25" fill="var(--navy)"/>
      </g>
      <g class="icons">
        <g transform="translate(364,137)"><circle r="9.5" fill="var(--aqua)"/><path d="M0,6 C-4,1 -4.5,-1 -4.5,-2 A4.5,4.5 0 1 1 4.5,-2 C4.5,-1 4,1 0,6Z" fill="#fff"/><circle cy="-2" r="1.8" fill="var(--aqua)"/></g>
        <g transform="translate(364,210)"><circle r="9.5" fill="var(--aqua)"/><rect x="-5" y="-1" width="10" height="5" rx="1" fill="#fff"/><path d="M-6,-2 Q0,-7 6,-2" stroke="#fff" stroke-width="2" fill="none"/></g>
        <g transform="translate(364,238)"><circle r="9.5" fill="var(--aqua)"/><rect x="-5" y="-2" width="10" height="6" rx="1" fill="#fff"/><rect x="-3" y="-6" width="6" height="4" fill="#fff"/></g>
        <g transform="translate(364,266)"><circle r="9.5" fill="var(--aqua)"/><path d="M-3,-6 L-1,-3 L-2,-1 Q0,3 2,4 L4,3 L6,5 L4,7 Q-6,3 -5,-5Z" fill="#fff"/></g>
        <g transform="translate(364,298)"><circle r="9.5" fill="var(--aqua)"/><path d="M-3,-6 L5,2 L1,2 L3,6 L1,7 L-1,3 L-3,5Z" fill="#fff"/></g>
      </g>
    </svg>
    <div class="badge badge--round">Velmar<br>Industrial Coatings</div>
    <p class="holder holder__name"><b>REED</b> <span>HALVORSEN</span></p>
    <p class="holder holder__phone">1-800-555-0142</p>
    <h1 class="company"><span class="company__lead">VELMAR</span><span class="company__line">INDUSTRIAL COATING INC.</span></h1>
    <p class="contact contact__office"><strong>Velmar Inc.</strong>PO.Box 412<br>Carden, WA 98000</p>
    <p class="contact__row" style="top:199px">(360) 555-0131</p>
    <p class="contact__row" style="top:227px">(360) 555-0133</p>
    <p class="contact__row" style="top:255px">(360) 555-0177</p>
    <p class="contact__row" style="top:287px">www.velmarfloors.com</p>
  </section>

  <!-- Back, navy -->
  <section class="card card--back-navy">
    <svg class="art" viewBox="0 0 596 358" aria-hidden="true">
      <g stroke="var(--aqua)" stroke-width="17" fill="none" stroke-linecap="round" stroke-linejoin="round">
        <polyline points="545,-8 506,25 568,87 605,52"/>
        <polyline points="-8,340 47,283 107,341 95,372"/>
      </g>
    </svg>
    <div class="badge badge--round">Velmar<br>Industrial Coatings</div>
  </section>

  <!-- Front, white -->
  <section class="card card--front-white">
    <svg class="art" viewBox="0 0 597 358" aria-hidden="true">
      <g stroke="var(--deco-grey)" stroke-width="16" fill="none" stroke-linecap="round" stroke-linejoin="round">
        <polyline points="485,-5 548,57 605,2"/>
        <polyline points="-8,245 58,310 10,365"/>
      </g>
      <g stroke="var(--grid-grey)" stroke-width="1.4" fill="none">
        <line x1="0" y1="60" x2="282" y2="60"/><line x1="0" y1="109" x2="338" y2="109"/>
        <line x1="0" y1="159" x2="338" y2="159"/><line x1="0" y1="208" x2="338" y2="208"/>
        <line x1="28" y1="60" x2="28" y2="208"/><line x1="75" y1="43" x2="75" y2="232"/>
        <line x1="143" y1="43" x2="143" y2="232"/><line x1="213" y1="43" x2="213" y2="232"/>
        <line x1="282" y1="43" x2="282" y2="232"/><line x1="329" y1="159" x2="329" y2="208"/>
        <line x1="0" y1="313" x2="282" y2="313"/>
        <line x1="27" y1="313" x2="27" y2="358"/><line x1="74" y1="297" x2="74" y2="358"/>
        <line x1="143" y1="297" x2="143" y2="358"/><line x1="212" y1="297" x2="212" y2="358"/>
        <line x1="280" y1="297" x2="280" y2="358"/>
      </g>
      <g class="info-panels">
        <rect x="364" y="122" width="233" height="70" fill="var(--teal-deep)"/>
        <rect x="364" y="192" width="233" height="3" fill="var(--white)"/>
        <rect x="364" y="196" width="233" height="85" fill="var(--teal-deep)"/>
        <rect x="364" y="281" width="233" height="3" fill="var(--white)"/>
        <rect x="364" y="285" width="233" height="25" fill="var(--teal-deep)"/>
      </g>
      <g class="icons">
        <g transform="translate(364,137)"><circle r="9.5" fill="var(--aqua)"/><path d="M0,6 C-4,1 -4.5,-1 -4.5,-2 A4.5,4.5 0 1 1 4.5,-2 C4.5,-1 4,1 0,6Z" fill="#fff"/><circle cy="-2" r="1.8" fill="var(--aqua)"/></g>
        <g transform="translate(364,210)"><circle r="9.5" fill="var(--aqua)"/><rect x="-5" y="-1" width="10" height="5" rx="1" fill="#fff"/><path d="M-6,-2 Q0,-7 6,-2" stroke="#fff" stroke-width="2" fill="none"/></g>
        <g transform="translate(364,238)"><circle r="9.5" fill="var(--aqua)"/><rect x="-5" y="-2" width="10" height="6" rx="1" fill="#fff"/><rect x="-3" y="-6" width="6" height="4" fill="#fff"/></g>
        <g transform="translate(364,266)"><circle r="9.5" fill="var(--aqua)"/><path d="M-3,-6 L-1,-3 L-2,-1 Q0,3 2,4 L4,3 L6,5 L4,7 Q-6,3 -5,-5Z" fill="#fff"/></g>
        <g transform="translate(364,298)"><circle r="9.5" fill="var(--aqua)"/><path d="M-3,-6 L5,2 L1,2 L3,6 L1,7 L-1,3 L-3,5Z" fill="#fff"/></g>
      </g>
    </svg>
    <div class="badge badge--square">Velmar<br>Industrial Coatings</div>
    <p class="holder holder__name"><b>REED</b> <span>HALVORSEN</span></p>
    <p class="holder holder__phone">1-800-555-0142</p>
    <h2 class="company"><span class="company__lead">VELMAR</span><span class="company__line">INDUSTRIAL COATING INC.</span></h2>
    <p class="contact contact__office"><strong>Velmar Inc.</strong>PO.Box 412<br>Carden, WA 98000</p>
    <p class="contact__row" style="top:199px">(360) 555-0131</p>
    <p class="contact__row" style="top:227px">(360) 555-0133</p>
    <p class="contact__row" style="top:255px">(360) 555-0177</p>
    <p class="contact__row" style="top:287px">www.velmarfloors.com</p>
  </section>

  <!-- Back, sky -->
  <section class="card card--back-sky">
    <svg class="art" viewBox="0 0 596 358" aria-hidden="true">
      <g stroke="var(--sky-deep)" stroke-width="17" fill="none" stroke-linecap="round" stroke-linejoin="round">
        <polyline points="545,-8 506,25 568,87 605,52"/>
        <polyline points="-8,340 47,283 107,341 95,372"/>
      </g>
    </svg>
    <div class="badge badge--round">Velmar<br>Industrial Coatings</div>
  </section>

</main>
</body>
</html>
```